Website Design Requirements

Domain Name: HometownTradesfolkRegistry.com

Website Look: Simple, Clean, Modern, and Professional Awarding Winning Website. Our Platform is the Best Directory Platform, all we need is a very creative person to make the following designs and select the fonts, font sizing, font colors and all the colors for the color points. We will follow up with the winner of the contest to design the rest of our design needs. The highlight of our brand is our Mascot; we feel this is something everyone will remember. It may be the easiest to obtain a free trial of the platform from Vantory Listings to complete this project. When we pick a winner of this contest we will provide the password to our admin panel for everything to be applied. Our Competitors are Perrows Hub, Yardwise Pro and Gravelnook.

We are thinking a light gray scale shadowing or graduated ghosting for the background behind the image of the Mascot for the main image. We want the Mascot and the Selection box to stand out as well as the logo.

Design Elements:
Main Page Image-Size for website is 1800 X 600px should be the Mascot on the right half of the image; this is where creative design is the most important. Design can use the head only from the waist up or the full image

Logo- Size for website is 450 X 70px; the logo should have the head of the mascot on a 3D icon with 2 line of text to the right side. The top line should have Hometown Tradesfolk the second line should have the word Directory in smaller size and be ghosted. The main idea about the logo is the icon and the words Hometown Tradesfolk. Note example can be seen on the Vantory Listings Rapid Launch Walkthrough on Clip Vue.

Favicon- Size for website is 56 X 56px should be the head of the mascot the Favicon and Google Map Pin drop could be the same if design is nice enough

Google Map Pin Drop- 25 X 46px should be the head of the mascot with a arrow pointing down.

Member Badge Image- Size 250 X 250px should be the head of the mascot inside a round ring with the words Verified –Certified –Member.

Target Market(s)

Consumers will use this website to locate Contractors in their Local area. Contractors will list their business on this website for a fee.

Industry/Entity Type

Domain

Contact Information for Business Card

Marcus Oldfield
Partner
555.014.2871
Marcus@HometownTradesfolkRegistry.Com
WWW. HometownTradesfolkRegistry.com

Logo Text

Hometown Tradesfolk Registry

Number of Pages Required

3 page

Font styles to use
Serif

Colors
ec1f27
fbed22

Requirements
Must have
• The use of our mascot, you can use full body view, waist up or head shot
Nice to have
• Clean bright colored Mascot, listing on back of card
• Hometown Tradesfolk
• Electricians
• Plumbers
• HVAC
• Landscapers
• General Contractors
• Garage Door Repair
• Carpet Cleaners
• Concrete Contractors

```html
<!DOCTYPE html>
<html lang="en">
<head>
<meta charset="utf-8">
<title>Hometown Tradesfolk Registry</title>
<link rel="stylesheet" href="https://fonts.googleapis.com/css2?family=Roboto+Condensed:wght@400;700&family=Roboto:wght@400;700&display=swap">
<style>
:root{
  --red:#b8100f;
  --red-title:#c8171d;
  --orange:#e8a200;
  --orange-deep:#d99400;
  --gray-dark:#3f3f3f;
  --text:#3a3a3a;
  --white:#ffffff;
}
*{box-sizing:border-box;margin:0;padding:0}
html,body{width:1200px;height:2639px;overflow:hidden;background:#fff}
body{position:relative;font-family:"Roboto",Arial,sans-serif;color:var(--text)}

/* header */
.site-header{position:absolute;left:0;top:0;width:1200px;height:72px;background:#fff}
.brand{position:absolute;left:252px;top:14px;display:flex;align-items:center;gap:10px}
.brand-dot{width:40px;height:40px;border-radius:50%;background:var(--orange)}
.brand-name{font-family:"Roboto Condensed",sans-serif;font-weight:700;font-size:14px;line-height:16px;letter-spacing:1.5px;color:var(--red-title);text-transform:uppercase;width:200px}
.contact-line{position:absolute;top:18px;text-align:center;font-family:"Roboto Condensed",sans-serif;color:var(--gray-dark)}
.contact-line small{display:block;font-size:11px;letter-spacing:1px}
.contact-line b{display:block;font-size:16px;letter-spacing:2px;font-weight:700}

/* nav */
.main-nav{position:absolute;left:0;top:72px;width:1200px;height:30px;background:var(--orange)}
.main-nav a{position:absolute;top:0;height:30px;line-height:30px;font-family:"Roboto Condensed",sans-serif;font-size:10px;letter-spacing:1.5px;color:#fff;text-decoration:none;font-weight:700}
.main-nav a.active{background:var(--red);width:98px;text-align:center}

/* hero */
.hero{position:absolute;left:0;top:102px;width:1200px;height:422px;background:linear-gradient(90deg,#3a3a3a 0%,#7d7d7d 55%,#9b9b9b 72%,#5b5b5b 100%);overflow:hidden}
.hero-photo{position:absolute;left:0;top:0;width:580px;height:422px;background:radial-gradient(ellipse at 45% 55%,#d8a233 0%,#a7742a 35%,#5a4a3a 70%,#3a3a3a 100%)}
.hero-copy{position:absolute;left:600px;top:80px;width:340px;color:#fff}
.hero-copy h1{font-family:"Roboto Condensed",sans-serif;font-size:23px;letter-spacing:3.5px;font-weight:400;line-height:28px;white-space:nowrap}
.hero-copy h2{font-family:"Roboto Condensed",sans-serif;font-size:12px;letter-spacing:2.5px;font-weight:700;margin-bottom:8px}
.hero-copy p{font-size:9.5px;line-height:12.5px;letter-spacing:.6px;margin-bottom:10px}
.cta{position:absolute;left:604px;top:306px;width:228px;height:30px;display:flex}
.cta span{flex:1;background:var(--orange);color:#fff;font-family:"Roboto Condensed",sans-serif;font-size:12px;letter-spacing:2.5px;line-height:30px;text-align:center;font-weight:700}
.cta i{width:32px;background:var(--red);display:flex;align-items:center;justify-content:center}
.verified{position:absolute;left:0;top:391px;width:375px;height:31px;background:var(--orange);clip-path:polygon(0 0,340px 0,375px 100%,0 100%);color:#fff;font-family:"Roboto Condensed",sans-serif;font-weight:700;font-size:15px;letter-spacing:3.5px;line-height:31px;padding-left:20px}
.slider-dots{position:absolute;left:540px;top:400px;display:flex;gap:6px}
.slider-dots span{width:8px;height:8px;border-radius:50%;background:#fff;opacity:.6}
.slider-dots span:first-child{opacity:1}
.mascot{position:absolute;left:950px;top:9px;width:215px;height:500px;background:linear-gradient(180deg,#e9b63c 0%,#c9433a 100%);opacity:.92;z-index:5}

/* feature strip */
.features{position:absolute;left:0;top:524px;width:1200px;height:83px;background:var(--red)}
.feature{position:absolute;top:0;height:83px;text-align:center;color:#fff;font-family:"Roboto Condensed",sans-serif}
.feature svg{display:block;margin:6px auto 2px}
.feature b{display:block;font-size:14px;letter-spacing:3px}
.feature small{display:block;font-size:10px;letter-spacing:2px}
.feature.mid{background:var(--orange)}

/* section titles */
.sec-title{position:absolute;left:0;width:1200px;text-align:center;font-family:"Roboto Condensed",sans-serif;font-weight:700;font-size:31px;letter-spacing:4px;color:var(--red-title)}
.sec-sub{position:absolute;left:0;width:1200px;text-align:center;font-family:"Roboto Condensed",sans-serif;font-weight:700;font-size:19px;letter-spacing:3px;color:var(--orange-deep)}
.para{position:absolute;left:278px;width:644px;text-align:center;font-size:9.8px;line-height:13px;color:var(--text)}
.read-more{position:absolute;left:540px;top:910px;width:122px;height:25px;border:1px solid #999;font-family:"Roboto Condensed",sans-serif;font-size:9px;letter-spacing:2px;color:#555;text-align:center;line-height:23px}

/* what we do */
.what{position:absolute;left:0;top:964px;width:1200px;height:440px;background:linear-gradient(90deg,#d9a12a 0%,#e5aa1e 40%,#e2a418 70%,#d49a22 100%)}
.what .sec-title,.what .sec-sub,.what .para{color:#fff}
.card{position:absolute;top:159px;width:215px}
.card-photo{width:215px;height:141px;border:3px solid #fff;background:linear-gradient(160deg,#6f9cc8 0%,#d8b070 55%,#b07a3a 100%)}
.card h3{font-family:"Roboto Condensed",sans-serif;font-size:13px;letter-spacing:2px;color:#fff;margin-top:8px}
.card p{font-size:8.5px;line-height:11px;color:#fff;margin-top:3px;width:205px}
.card em{display:block;font-style:normal;font-family:"Roboto Condensed",sans-serif;font-size:9px;letter-spacing:1.5px;color:#fff;font-weight:700;margin-top:8px}

/* our work */
.work-grid{position:absolute;left:250px;top:1543px;width:702px;height:287px}
.tile{position:absolute;width:144px;height:143px;overflow:hidden}
.tile-photo{background:linear-gradient(160deg,#e9b84a 0%,#b8a088 45%,#5e7ea6 100%)}
.tile-text{background:#fff;padding:10px 8px}
.tile-text time{display:block;font-size:8px;color:#777;letter-spacing:1px}
.tile-text h4{font-family:"Roboto Condensed",sans-serif;font-size:11.5px;line-height:13px;letter-spacing:1.5px;color:var(--red-title);margin:4px 0}
.tile-text p{font-size:7.5px;line-height:9.5px;color:#555}
.plus{position:absolute;color:#fff;font-size:14px;font-weight:700;line-height:14px}
.plus.dark{color:#222}
.feature-tile{position:absolute;left:0;top:0;width:269px;height:287px;background:linear-gradient(180deg,#c84a2a 0%,#b8201a 55%,#a8120f 100%);color:#fff;padding:160px 12px 0}
.feature-tile time{font-size:9px;letter-spacing:2px}
.feature-tile h4{font-family:"Roboto Condensed",sans-serif;font-size:17px;line-height:20px;letter-spacing:3px;margin:4px 0}
.feature-tile p{font-size:8px;line-height:10.5px}

/* testimonials */
.testimonials{position:absolute;left:0;top:1936px;width:1200px;height:303px;background:linear-gradient(90deg,#b8272b 0%,#d0393a 45%,#c4302f 70%,#b42528 100%);color:#fff;text-align:center}
.avatar{position:absolute;left:544px;top:1872px;width:112px;height:112px;border-radius:50%;border:5px solid #fff;background:linear-gradient(180deg,#e9b84a 0%,#b8a088 55%,#6a8fb8 100%);box-shadow:0 2px 6px rgba(0,0,0,.3);z-index:3}
.testimonials h2{position:absolute;top:62px;width:1200px;font-family:"Roboto Condensed",sans-serif;font-size:32px;letter-spacing:6px;font-weight:400}
.testimonials p{position:absolute;left:288px;top:114px;width:624px;font-size:10px;line-height:14px;letter-spacing:.5px}
.testimonials .who{position:absolute;top:192px;width:1200px;font-family:"Roboto Condensed",sans-serif;font-size:14px;letter-spacing:2px}
.testimonials .role{position:absolute;top:211px;width:1200px;font-size:9px;font-style:italic;letter-spacing:1px}
.t-dots{position:absolute;left:584px;top:230px;display:flex;gap:4px}
.t-dots span{width:9px;height:9px;background:#fff;opacity:.6}
.t-dots span:first-child{opacity:1}

/* contact footer */
.contact{position:absolute;left:0;top:2239px;width:1200px;height:327px;background:linear-gradient(90deg,#e2a41c 0%,#e9ad20 50%,#dfa019 100%);color:#fff}
.socials{position:absolute;left:478px;top:2214px;display:flex;gap:20px;z-index:3}
.socials span{width:48px;height:48px;border-radius:50%;background:#fff;color:var(--red-title);font-family:"Roboto Condensed",sans-serif;font-size:8.5px;font-weight:700;display:flex;align-items:center;justify-content:center}
.contact .name{position:absolute;left:273px;top:52px;font-family:"Roboto Condensed",sans-serif;font-size:19px;letter-spacing:4px}
.contact .reach{position:absolute;right:276px;top:50px;text-align:right;font-family:"Roboto Condensed",sans-serif}
.contact .reach small{display:block;font-size:12px;letter-spacing:1px}
.contact .reach b{display:block;font-size:17px;letter-spacing:2px;font-weight:400}
.contact h2{position:absolute;top:97px;width:1200px;text-align:center;font-family:"Roboto Condensed",sans-serif;font-size:27px;letter-spacing:5px;font-weight:400}
.contact p{position:absolute;left:318px;top:138px;width:564px;text-align:center;font-size:9px;line-height:12px}
.field{position:absolute;height:28px;background:#f5f5f5;font-family:"Roboto Condensed",sans-serif;font-size:8px;letter-spacing:1.5px;color:#888;padding:9px 10px}
.send{position:absolute;left:535px;top:294px;width:132px;height:28px;background:var(--red);font-family:"Roboto Condensed",sans-serif;font-size:10px;letter-spacing:2px;line-height:28px;text-align:center}

.footer-nav{position:absolute;left:0;top:2566px;width:1200px;height:39px;background:var(--orange-deep)}
.footer-nav a{position:absolute;top:11px;height:18px;line-height:18px;font-family:"Roboto Condensed",sans-serif;font-size:9.5px;letter-spacing:1.5px;color:#fff;text-decoration:none;font-weight:700}
.footer-nav a.active{background:var(--red);width:69px;text-align:center}
.copyright{position:absolute;left:0;top:2605px;width:1200px;height:34px;background:var(--red);color:#fff;font-size:9px;letter-spacing:.6px;line-height:34px;padding-left:272px}
</style>
</head>
<body>

<header class="site-header">
  <div class="brand"><span class="brand-dot"></span><span class="brand-name">Hometown Tradesfolk Registry</span></div>
  <div class="contact-line" style="left:600px"><small>Fax Number:</small><b>(555) 014-5569</b></div>
  <div class="contact-line" style="left:795px"><small>Phone Number:</small><b>(555) 014-5570</b></div>
</header>

<nav class="main-nav">
  <a class="active" style="left:250px">HOME</a>
  <a style="left:370px">WHAT WE DO</a>
  <a style="left:482px">WHO WE ARE</a>
  <a style="left:592px">OUR WORK</a>
  <a style="left:690px">BLOG</a>
  <a style="left:760px">TESTIMONIALS</a>
  <a style="left:880px">CONTACT US</a>
</nav>

<div class="mascot" role="img" aria-label="Mascot illustration: full-body tradesman in hard hat and tool belt, arms crossed"></div>

<section class="hero">
  <div class="hero-photo" role="img" aria-label="Photo of gloved hands holding a tool belt filled with hand tools"></div>
  <div class="hero-copy">
    <h1>HOMETOWN TRADESFOLK</h1>
    <h2>PLATFORM FROM VANTORY LISTINGS</h2>
    <p>Lorem Ipsum simply dummy text of the printing and typeset lipsum ting industry. Lorem Ipsum has been the industry standard dummy text ever since the 1500s, when an unknown printer took a galley of type and scrambled it to make a type specimen book. Lorem Ipsum simply dummy text of the printing and typeset industry, since the 1500s, when an unknown printer.</p>
    <p>Lorem Ipsum simply dummy text of the printing and typeset lipsum ting industry. Lorem Ipsum has been the industry standard dummy text ever since the 1500s, when an unknown printer.</p>
  </div>
  <div class="cta"><span>GET STARTED TODAY!</span><i><svg width="12" height="12" viewBox="0 0 12 12"><path d="M2 2l4 4 4-4M2 6l4 4 4-4" fill="none" stroke="#fff" stroke-width="1.6"/></svg></i></div>
  <div class="verified">VERIFIED –CERTIFIED –MEMBER</div>
  <div class="slider-dots"><span></span><span></span><span></span></div>
</section>

<section class="features">
  <div class="feature" style="left:250px;width:239px">
    <svg width="34" height="34" viewBox="0 0 34 34"><circle cx="14" cy="14" r="10" fill="none" stroke="#fff" stroke-width="3"/><path d="M21 21l10 10" stroke="#fff" stroke-width="4" stroke-linecap="round"/></svg>
    <b>SEARCH</b><small>SEARCH TO FIND MEMBERS</small>
  </div>
  <div class="feature mid" style="left:489px;width:233px">
    <svg width="34" height="34" viewBox="0 0 34 34"><circle cx="17" cy="17" r="14" fill="none" stroke="#fff" stroke-width="2.5"/><circle cx="17" cy="13" r="4" fill="#fff"/><path d="M10 25c1-5 4-7 7-7s6 2 7 7z" fill="#fff"/></svg>
    <b>REVIEW</b><small>COMPARE MEMBERS YOUR FIND</small>
  </div>
  <div class="feature" style="left:722px;width:240px">
    <svg width="34" height="34" viewBox="0 0 34 34"><circle cx="24" cy="8" r="4" fill="#fff"/><circle cx="9" cy="17" r="4" fill="#fff"/><circle cx="24" cy="26" r="4" fill="#fff"/><path d="M24 8L9 17l15 9" fill="none" stroke="#fff" stroke-width="2"/></svg>
    <b>CONNECT</b><small>CONTACT MEMBERS YOU LIKE</small>
  </div>
</section>

<section class="who">
  <h2 class="sec-title" style="top:634px">WHO WE ARE</h2>
  <h3 class="sec-sub" style="top:672px">VANTORY LISTINGS QUICK START GUIDE</h3>
  <p class="para" style="top:718px">Maecenas accumsan tincidunt neque, egeignissim augueulvutpat eu. Sedmmsan tincidussa augue, eleifend in eros eu, ullamcorper ullamcorper tellus. Nam et sagittis dolor. Cras consequat vitae tellus vitae tempus. Nulla imperdiet, dui vitae rutrum finibus, sapien ante condimentum sapien, eu bibendum neque leo sed magna. Praesent tincidunt elit orci, quis maximus purus posuere id.</p>
  <p class="para" style="top:772px">Praesent lacinia dignissim eros at ultricies. Maecenas accumsan tincidunt neque, eget dignissim augue volutpat eu. Sed massa augue, eleifend in eros eu, ullamcorper ullamcorper tellus. Nam et sagittis dolor. Cras consequat vitae tellus vitae tempus. Nulla imperdiet, dui vitae rutrum finibus, sapien ante condimentum sapien, eu bibendum neque leo sed magna.</p>
  <p class="para" style="top:832px">Praesent tincidunt elit orci, quis maximus purus posuere ident lacinia dignissim eros at ultricies. Maecenas accumsan tincidunt neque, eget dignissim augue volutpat eu. Sed massa augue odio dignissim, sollicitudin aliquam felis pharetra. Vivamus nisl magna, rutrum sit amet orci sit amet, ue, eleifend in eros eu, ullamcorper ullamcorper tellus. Nam et sagittis dolor. Cras consequat odio dignissim, sollicitudin a maximus tincidunt purus posuere id. Praesent lacinia dignissim eros at ultricies.</p>
  <div class="read-more">READ MORE</div>
</section>

<section class="what">
  <h2 class="sec-title" style="top:36px;font-weight:400;letter-spacing:6px;font-size:29px">WHAT WE DO</h2>
  <h3 class="sec-sub" style="top:73px;font-weight:400">GET EVERYTHING WE OFFER FOR ONE SIMPLE PRICE</h3>
  <p class="para" style="top:106px">Maecenas accumsan tincidunt neque, egeignissim augueulvutpat eu. Sedmmsan tincidussa augue, eleifend in eros eu, ullamcorper ullamcorper tellus. Nam et sagittis dolor. Cras consequat vitae tellus vitae tempus. Nulla imperdiet, dui vitae rutrum finibus, sapien ante condimentum sapien, eu bibendum neque leo sed magna. Praesent tincidunt elit orci</p>
  <div class="card" style="left:250px">
    <div class="card-photo" role="img" aria-label="Photo of a worker in checked shirt with gloved arms crossed"></div>
    <h3>TOP TIPS FOR MANAGING</h3>
    <p>Hometown Tradesfolk vivas, ulamcper ullamcorper tellusm et sagittis dolesegec odio dignissim, sollicitudin eros eu.</p>
    <em>Read More</em>
  </div>
  <div class="card" style="left:491px">
    <div class="card-photo" role="img" aria-label="Photo of a worker in hard hat and overalls beside a vehicle"></div>
    <h3>TOP TIPS FOR MANAGING</h3>
    <p>Hometown Tradesfolk vivas, ulamcper ullamcorper tellusm et sagittis dolesegec odio dignissim, sollicitudin eros eu.</p>
    <em>Read More</em>
  </div>
  <div class="card" style="left:732px">
    <div class="card-photo" role="img" aria-label="Photo of a builder in hard hat carrying timber"></div>
    <h3>TOP TIPS FOR MANAGING</h3>
    <p>Hometown Tradesfolk vivas, ulamcper ullamcorper tellusm et sagittis dolesegec odio dignissim, sollicitudin eros eu.</p>
    <em>Read More</em>
  </div>
</section>

<section class="work">
  <h2 class="sec-title" style="top:1427px">OUR WORK</h2>
  <h3 class="sec-sub" style="top:1465px">VANTORY LISTINGS QUICK START GUIDE</h3>
  <p class="para" style="top:1504px">Maecenas accumsan tincidunt neque, egeignissim augueulvutpat eu. Sedmmsan tincidussa augue, eleifend in eros eu, ullamcorper ullamcorper tellus vitae tellus vitae temtae rutrum finibus, sapien ante condimentum sapien, eu bibendum neque leo se</p>
  <div class="work-grid">
    <div class="feature-tile" role="img" aria-label="Photo of a contractor in hard hat with red overlay">
      <time>20 /SEPTEMBER / 2016</time>
      <h4>HOMETOWN TRADESFOLK DIRECTOR</h4>
      <p>Lorem Ipsum is simply dummy text of the printing and typesetting industry. Lorem Ipsum has been the industry's standard dummy text ever since the 1500s, when an unknown printer took a galley of type and scrambled it to make a type specimen book.</p>
    </div>
    <span class="plus" style="left:253px;top:4px">+</span>
    <div class="tile tile-photo" style="left:269px;top:0" role="img" aria-label="Photo of a tradesman holding a tool belt"></div>
    <div class="tile tile-text" style="left:413px;top:0"><time>24/ OCTOBER / 2016</time><h4>TOP 10 HOMETOWN TRADESFOLK</h4><p>Praesent tincidunt elit orci, quis maximus purus posuere ident acinia ignissimeros accumsan tincidunt neget. Tignissimus posuere id acinia ignissimeros accumsan.</p></div>
    <span class="plus dark" style="left:546px;top:4px">+</span>
    <div class="tile tile-photo" style="left:558px;top:0" role="img" aria-label="Photo of a worker in hard hat"></div>
    <div class="tile tile-text" style="left:269px;top:144px"><time>24/ OCTOBER / 2016</time><h4>TOP 10 HOMETOWN TRADESFOLK</h4><p>Praesent tincidunt elit orci, quis maximus purus posuere ident acinia ignissimeros accumsan tincidunt neget. Tignissimus posuere id acinia.</p></div>
    <span class="plus dark" style="left:401px;top:148px">+</span>
    <div class="tile tile-photo" style="left:413px;top:144px" role="img" aria-label="Photo of a worker in overalls on a ladder"></div>
    <div class="tile tile-text" style="left:558px;top:144px"><time>24/ OCTOBER / 2016</time><h4>TOP 10 HOMETOWN TRADESFOLK</h4><p>Praesent tincidunt elit orci, quis maximus purus posuere ident acinia ignissimeros accumsan tincidunt neget. Tignissimus posuere id acinia.</p></div>
    <span class="plus dark" style="left:690px;top:148px">+</span>
  </div>
</section>

<div class="avatar" role="img" aria-label="Portrait photo of a builder in hard hat"></div>
<section class="testimonials" aria-label="Testimonials">
  <h2>TESTIMONIALS</h2>
  <p>Sed massa augnec odio dignissim, sollicitudin aliquam felis pharetra. Vivamus nisl magna, rutrum sit amet orci sit amet, ue, eleifend in eros eullamcorpsim, ullamcorpsim, sollicitudin aliquam felis per ullamcorper tellus. Namet sagittis dolorac consequec odiodignissimed massa augnec odio dignmagna, rutrum sit amet orci sit amet, ue, eleifend in eros euullamcorpsim, sollicitudin aliquam felis per ullamcorpelte luam et sagittisdolorac consequec odiousim, sollicitudin asollictid.</p>
  <div class="who">Dale Hursley</div>
  <div class="role">Building Worker</div>
  <div class="t-dots"><span></span><span></span><span></span></div>
</section>

<div class="socials"><span>Pagebook</span><span>Linkora</span><span>Chirply</span><span>Plusway</span></div>
<section class="contact">
  <div class="name">HOMETOWN TRADESFOLK</div>
  <div class="reach"><small>info@HometownTradesfolkRegistry.com</small><b>(555) 014-5570</b></div>
  <h2>CONTACT US</h2>
  <p>Sed massa augnec odio dignissim, sollicitudin aliquam felis pharetra magna, rutrum sit amet orci sit amet, ue, eleifend in eu, ullamcorpsim, sollicitudin aliquam felis per ullamcor sagittis dolor. Cras consequec odio dignissim, sollicitudin a</p>
  <div class="field" style="left:269px;top:174px;width:208px">YOUR NAME</div>
  <div class="field" style="left:496px;top:174px;width:208px">YOUR EMAIL</div>
  <div class="field" style="left:722px;top:174px;width:207px">YOUR PHONE</div>
  <div class="field" style="left:269px;top:216px;width:660px;height:65px">THE MESSAGE</div>
  <div class="send">SEND THE MESSAGE</div>
</section>

<nav class="footer-nav">
  <a class="active" style="left:271px">HOME</a>
  <a style="left:362px">WHO WE ARE</a>
  <a style="left:479px">WHAT WE DO</a>
  <a style="left:592px">OUR WORK</a>
  <a style="left:692px">BLOG</a>
  <a style="left:761px">TESTIMONIALS</a>
  <a style="left:881px">CONTACT US</a>
</nav>
<footer class="copyright">© Copyright 2016 Hometown Tradesfolk Registry. All rights reserved. | Terms | Sitemap | Login</footer>

</body>
</html>
```